Restyle Company web site and logo

we need a wordpress design beacause after few year we need to refresh our company web site(www.velantoworks.net) & logo. We are a small company called KR Advisory focused on business intellegence, data quality, data integration, etc and based on Legnago (small town near to Verona (italy)).
During the 2014 we add to our skill develop project for MDM and Procurement.
We are Young (avg 30 years old). We want to change our logo and color templete to communicate to all cumstomer professional skill, precision and passion.

--- UPDATE --
The new site can be complitile different from the actual website.
The new Logo is now available.

Target Market(s)

B2B, mid size market, professional account

Industry/Entity Type

It Company

Font styles to use
Sans Serif

Colors
acd037
3277b5

Requirements
Must have
• Simple and clean/clear image colur. Professional site. it need to rapresent trust site.
• Must be responsive desk/mobile.
Nice to have
• different color area for different kind off business line.
• slider image.
Should not have
• classical image

```html
<!DOCTYPE html>
<html lang="it">
<head>
<meta charset="utf-8">
<title>KR Advisory – Home e Contatti</title>
<link href="https://fonts.googleapis.com/css2?family=Lato:wght@300;400;700&display=swap" rel="stylesheet">
<style>
:root{
  --green:#a0c800;
  --green-text:#9cc21a;
  --blue:#23628f;
  --stage:#6d6d6d;
  --white:#ffffff;
  --text:#8a8a8a;
  --text-dark:#555;
  --line:#c9c9c9;
}
*{box-sizing:border-box;margin:0;padding:0}
html,body{width:1200px;height:1000px;overflow:hidden;background:var(--white);font-family:'Lato',sans-serif}
.stage{position:absolute;left:0;top:0;width:1200px;height:745px;background:var(--stage)}
.page{position:absolute;top:0;background:var(--white);overflow:hidden}
.page--home{left:28px;width:540px;height:720px}
.page--contact{left:623px;width:543px;height:745px}
.topbar{position:absolute;left:0;top:0;width:100%;height:20px;background:var(--green)}
.topbar .social{position:absolute;top:4px;width:11px;height:11px;border-radius:50%;background:var(--white)}
.brand{position:absolute;left:0;top:20px;width:100%;height:85px;display:flex;flex-direction:column;align-items:center;justify-content:center;gap:8px}
.brand-dot{width:34px;height:34px;border-radius:50%;background:var(--green)}
.brand-name{color:var(--blue);font-weight:700;font-size:13px;letter-spacing:.3px}
.nav{position:absolute;left:0;top:105px;width:100%;height:23px;background:var(--blue);display:flex;justify-content:center;align-items:center;gap:11px}
.nav a{color:var(--white);font-size:6.5px;font-weight:700;text-decoration:none;letter-spacing:.2px;line-height:23px}
.nav a.active{color:var(--green);box-shadow:inset 0 -2px 0 var(--green);line-height:17px}
.nav svg{width:7px;height:7px}
.hero{position:absolute;left:0;top:128px;width:540px;height:160px;background:linear-gradient(90deg,#5d6fa8 0%,#9aa7cf 45%,#c7c9d8 60%,#8e9cc6 100%)}
.hero-overlay{position:absolute;left:33px;top:0;width:474px;height:155px;background:rgba(150,165,210,.35);text-align:center;padding-top:30px}
.hero-title{color:var(--green);font-size:17px;font-weight:400}
.hero-text{color:var(--white);font-size:8.5px;font-weight:700;line-height:19px;margin-top:6px;padding:0 4px}
.intro-heading{position:absolute;left:20px;top:314px;width:500px;text-align:center;color:var(--green-text);font-size:11.5px;line-height:21px;font-weight:400}
.intro-text{position:absolute;left:26px;top:374px;width:470px;text-align:center;color:var(--text);font-size:7px;line-height:14px}
.intro-cta{position:absolute;left:0;top:428px;width:540px;text-align:center;color:var(--green-text);font-size:7.5px;font-weight:700}
.card{position:absolute;top:462px;width:106px;height:78px;background:var(--white);box-shadow:0 5px 7px rgba(0,0,0,.45)}
.card-badge{height:51px;margin:1px;background:#d8d8d8}
.card-title{color:var(--green-text);font-size:6.5px;padding:5px 0 0 6px}
.card-date{color:#9a9a9a;font-size:3.8px;padding:2px 0 0 6px}
.footer{position:absolute;left:0;top:588px;width:540px;height:132px;background:var(--green);text-align:center}
.footer-social{display:flex;justify-content:center;gap:14px;margin-top:31px}
.footer-social span{width:24px;height:24px;border-radius:50%;background:#d9ec9c}
.footer-nav{color:var(--white);font-size:5.5px;font-weight:700;margin-top:10px;letter-spacing:.3px}
.footer-legal{color:#d4ea86;font-size:5px;letter-spacing:.6px;line-height:9px;margin:12px auto 0;width:400px}
.page-title{position:absolute;left:27px;top:134px;color:var(--green-text);font-size:14px;letter-spacing:1px;font-weight:400}
.title-rule{position:absolute;left:0;top:156px;width:100%;height:1px;background:#eee}
.office{position:absolute;top:181px;color:var(--text-dark);font-size:7.3px;line-height:14px;font-style:normal}
.office strong{color:var(--green-text);font-weight:700}
.office .bullet{color:var(--green-text)}
.map{position:absolute;top:249px;width:234px;height:135px;background:linear-gradient(135deg,#ece9e1 0%,#e2ddd3 60%,#a9c4e3 100%)}
.form-intro{position:absolute;left:0;top:409px;width:543px;text-align:center;color:var(--green-text);font-size:7.3px;font-weight:700;line-height:14px}
.field-label{position:absolute;left:27px;color:var(--text-dark);font-size:6.8px}
.field{position:absolute;left:27px;width:489px;height:15px;border:1px solid var(--line);background:var(--white)}
.field--area{height:80px}
.send{position:absolute;left:27px;top:658px;width:38px;height:22px;background:var(--green);color:var(--white);font-size:6.8px;font-weight:700;text-align:center;line-height:22px;box-shadow:0 3px 4px rgba(0,0,0,.35)}
.bottom-band{position:absolute;left:0;top:731px;width:100%;height:14px;background:var(--green)}
</style>
</head>
<body>
<div class="stage">

  <section class="page page--home">
    <div class="topbar"><span class="social" style="left:482px"></span><span class="social" style="left:500px"></span></div>
    <div class="brand"><span class="brand-dot"></span><span class="brand-name">KR ADVISORY</span></div>
    <nav class="nav">
      <a class="active">HOME ▾</a><a>BUSINESS PARTNERS</a><a>REFERENZE</a><a>CONTATTI</a>
      <svg viewBox="0 0 10 10"><circle cx="4" cy="4" r="3" fill="none" stroke="#a0c800" stroke-width="1.5"/><line x1="6.2" y1="6.2" x2="9" y2="9" stroke="#a0c800" stroke-width="1.5"/></svg>
    </nav>
    <div class="hero" role="img" aria-label="Foto sfumata di un'operatrice di supporto con cuffie">
      <div class="hero-overlay">
        <h2 class="hero-title">Evolution support</h2>
        <p class="hero-text">Non lasciare che i problemi frenino il tuo business. Evolution support nasce con lo scopo di aiutare i nostri clienti in tutti i momenti di progetto, intervenendo a 360° su tutte le aree (software, supporto utenti, formazione, bug fixing)....</p>
      </div>
    </div>
    <h3 class="intro-heading">Quante persone all'interno della vostra azienda hanno l'informazione desiderata, nel momento giusto e nella forma corretta?</h3>
    <p class="intro-text">Per un'azienda è fondamentale sfruttare le innumerevoli informazioni di cui dispone rendendole consultabili ai propri manager al fine di aiutarli nella scelta delle giuste strategie aziendali (capire l'andamento delle performance dell'azienda, generare stime previsionali, ipotizzare scenari futuri e future strategie di risposta).</p>
    <p class="intro-cta">KR Advisory vi aiuta a gestire questo processo nel modo più semplice e veloce!</p>

    <article class="card" style="left:28px"><div class="card-badge" style="background:#6ea0d8"></div><p class="card-title">News Article One</p><p class="card-date">OCTOBER 2, 2014</p></article>
    <article class="card" style="left:154px"><div class="card-badge" style="background:#3b7fc4"></div><p class="card-title">News Article Two</p><p class="card-date">OCTOBER 2, 2014</p></article>
    <article class="card" style="left:280px"><div class="card-badge" style="background:#d4d4d4"></div><p class="card-title">News Article Three</p><p class="card-date">OCTOBER 2, 2014</p></article>
    <article class="card" style="left:406px"><div class="card-badge" style="background:#dfe4ea"></div><p class="card-title">News Article Four</p><p class="card-date">OCTOBER 1, 2014</p></article>

    <footer class="footer">
      <div class="footer-social"><span></span><span></span></div>
      <p class="footer-nav">HOME &nbsp;/&nbsp; BUSINESS PARTNERS &nbsp;/&nbsp; REFERENZE &nbsp;/&nbsp; CONTATTI</p>
      <p class="footer-legal">KR ADVISORY S.R.L. - CORSO AURELIO, 24/B - 37999 BORGOVERDE (BV) - P.IVA 00000000000 © COPYRIGHT KR ADVISORY S.R.L. 2014. ALL RIGHTS RESERVED.</p>
    </footer>
  </section>

  <section class="page page--contact">
    <div class="topbar" style="height:18px"><span class="social" style="left:486px;top:3px"></span><span class="social" style="left:503px;top:3px"></span></div>
    <div class="brand" style="top:18px;height:87px"><span class="brand-dot"></span><span class="brand-name">KR ADVISORY</span></div>
    <nav class="nav">
      <a>HOME ▾</a><a>BUSINESS PARTNERS</a><a>REFERENZE</a><a class="active">CONTATTI</a>
      <svg viewBox="0 0 10 10"><circle cx="4" cy="4" r="3" fill="none" stroke="#a0c800" stroke-width="1.5"/><line x1="6.2" y1="6.2" x2="9" y2="9" stroke="#a0c800" stroke-width="1.5"/></svg>
    </nav>
    <h1 class="page-title">CONTATTI</h1>
    <div class="title-rule"></div>

    <address class="office" style="left:27px"><strong>Sede LegaleVia</strong><br>Corso Aurelio, 24/B<br>37999 Borgoverde (BV)<br>Italy</address>
    <address class="office" style="left:281px"><strong>Sede LegaleVia</strong><br>Corso Aurelio, 112<br>37999 Borgoverde (BV)<br><span class="bullet">•</span> Tel 0123 - 5550198 &nbsp; <span class="bullet">•</span> Fax 0123 - 5550195</address>

    <div class="map" style="left:27px" role="img" aria-label="Mappa della sede in Corso Aurelio 24/B, Borgoverde"></div>
    <div class="map" style="left:281px" role="img" aria-label="Mappa della sede in Corso Aurelio 112, Borgoverde"></div>

    <p class="form-intro">Compila questo modulo per richiedere informazioni. Sarai ricontattato prima possibile.<br>Ti preghiamo di compilare tutti i campi obbligatori.</p>

    <label class="field-label" style="top:451px">Il tuo nome*</label><div class="field" style="top:462px"></div>
    <label class="field-label" style="top:487px">La tua email*</label><div class="field" style="top:498px"></div>
    <label class="field-label" style="top:524px">Numero di telefono</label><div class="field" style="top:535px"></div>
    <label class="field-label" style="top:560px">Descrivi la tua richiesta</label><div class="field field--area" style="top:571px"></div>
    <div class="send">Send</div>
    <div class="bottom-band"></div>
  </section>

</div>
</body>
</html>
```